Military training company needs a Powerpoint desk template.

We need a Powerpoint deck that we can use for sales and training purposes. We are a training company for military mountaineering, so need something simple, clean and uncluttered that incorporates our logo and includes a placeholder for our tagline (under development). The colors need to complement and/or include the colors in the logo that was designed by Brushquill (attached below)

Requirements
Must have
• We need a title slide, table of content, etc. Please use the fonts and colors in the logo.

```html
<!DOCTYPE html>
<html lang="en">
<head>
<meta charset="utf-8">
<title>Ridgeward Deck Template</title>
<link href="https://fonts.googleapis.com/css2?family=Anton&family=Roboto:wght@400;500;700&display=swap" rel="stylesheet">
<style>
:root{
  --page:#efdfcc;
  --navy:#1b2440;
  --tan:#a08869;
  --cream:#e3dec6;
  --ink:#1b2440;
  --muted:#6f6a5c;
  --light:#f3efe2;
}
*{margin:0;padding:0;box-sizing:border-box}
html,body{width:1200px;height:4051px;overflow:hidden;background:var(--page);font-family:"Roboto",Arial,sans-serif}
.slide{position:absolute;left:76px;width:1048px;height:590px;overflow:hidden;background:var(--cream);box-shadow:0 3px 10px rgba(60,40,20,.18)}
.slide svg.bg{position:absolute;inset:0}
.abs{position:absolute}
.brand{font-family:"Anton",Impact,sans-serif;color:var(--cream);letter-spacing:3px;display:flex;align-items:center;gap:6px;white-space:nowrap}
.brand .mark{width:8px;height:8px;background:var(--tan)}
.display{font-family:"Anton",Impact,sans-serif;letter-spacing:8px;color:var(--cream);white-space:nowrap}
.kicker{font-family:"Anton",Impact,sans-serif;color:var(--tan);letter-spacing:3px;font-size:15px}
.lead{color:#fff;font-size:16px;line-height:25px}
.photo{position:absolute}
.socials{display:flex;gap:25px}
.social{width:30px;height:30px;border:1.5px solid var(--cream);transform:rotate(45deg);display:flex;align-items:center;justify-content:center}
.social::after{content:"";width:6px;height:6px;background:var(--cream);border-radius:50%}
.header-title{position:absolute;left:100px;top:28px;font-family:"Anton",Impact,sans-serif;font-size:30px;letter-spacing:6px;color:var(--cream)}
.header-brand{position:absolute;left:773px;top:34px;font-size:16px}
.page-no{position:absolute;right:60px;top:560px;font-size:9px;font-weight:700;color:var(--ink);letter-spacing:.5px}
.footer-bar{position:absolute;left:0;bottom:0;height:5px;width:100%;background:linear-gradient(90deg,var(--navy) 0 800px,var(--tan) 800px)}
.agenda-item{position:absolute;left:106px;display:flex;align-items:center;gap:30px}
.num{width:38px;height:38px;display:flex;align-items:center;justify-content:center;position:relative;color:#fff;font-size:18px}
.num::before{content:"";position:absolute;inset:5px;background:var(--tan);transform:rotate(45deg)}
.num span{position:relative}
.agenda-label{font-size:19px;font-weight:500;color:var(--ink)}
.watermark{position:absolute;left:555px;top:210px;font-family:"Anton",Impact,sans-serif;font-size:68px;letter-spacing:8px;color:rgba(160,136,105,.18)}
.body-copy{font-size:12px;line-height:21px;color:var(--muted);text-align:justify}
.body-copy p{margin-bottom:12px}
.bullets{list-style:none}
.bullets li{position:relative;padding-left:36px;margin-bottom:14px;font-size:12px;line-height:21px;color:var(--muted);text-align:justify}
.bullets li::before{content:"";position:absolute;left:2px;top:5px;width:9px;height:9px;border:1.5px solid var(--tan);border-radius:50%}
.bullets li::after{content:"";position:absolute;left:6px;top:9px;width:4px;height:4px;background:var(--tan);border-radius:50%}
.feature-label{position:absolute;font-size:12px;font-weight:700;line-height:20px;color:var(--ink)}
.contact{position:absolute;right:58px;display:flex;align-items:center;gap:28px;color:#fff;font-size:17px;white-space:nowrap}
.contact .ico{width:40px;height:40px;position:relative;display:flex;align-items:center;justify-content:center}
.contact .ico::before{content:"";position:absolute;inset:6px;background:var(--tan);transform:rotate(45deg)}
.contact .ico svg{position:relative}
</style>
</head>
<body>

<!-- Slide 1: Title -->
<section class="slide" style="top:88px">
  <svg class="bg" width="1048" height="590">
    <polygon points="0,0 345,0 725,590 0,590" fill="var(--navy)"/>
  </svg>
  <div class="photo" role="img" aria-label="Soldier in field gear standing on a rocky summit overlooking a river valley under cloudy sky" style="inset:0;clip-path:polygon(345px 0,1048px 0,1048px 590px,725px 590px);background:linear-gradient(200deg,#dfe4dd 0%,#aeb7ad 35%,#5f6a56 65%,#3a3a2c 100%)"></div>
  <svg class="bg" width="1048" height="590">
    <line x1="341" y1="0" x2="721" y2="590" stroke="var(--cream)" stroke-width="8"/>
    <polygon points="522,300 718,590 330,590" fill="var(--tan)"/>
  </svg>
  <div class="abs brand" style="left:62px;top:40px;font-size:24px"><span class="mark"></span>RIDGEWARD</div>
  <div class="abs kicker" style="left:60px;top:212px">WELCOME TO</div>
  <div class="abs display" style="left:58px;top:238px;font-size:56px">RIDGEWARD</div>
  <p class="abs lead" style="left:60px;top:322px;width:385px">Lorem ipsum dolor sit amet, consectetur adipisc elit, sed do eiusmod temporea incididunt utla etdolore magna aliquea.</p>
  <div class="abs socials" style="left:69px;top:532px">
    <div class="social"></div><div class="social"></div><div class="social"></div><div class="social"></div>
  </div>
</section>

<!-- Slide 2: Agenda -->
<section class="slide" style="top:745px">
  <svg class="bg" width="1048" height="590">
    <polygon points="4,0 870,0 959,100 100,100" fill="var(--navy)"/>
    <polygon points="870,0 1048,0 1048,200" fill="var(--tan)"/>
  </svg>
  <div class="header-title">AGENDA</div>
  <div class="brand header-brand"><span class="mark"></span>RIDGEWARD</div>
  <div class="watermark">RIDGEWARD</div>
  <div class="agenda-item" style="top:143px"><div class="num"><span>1</span></div><div class="agenda-label">RIDGEWARD INTRODUCTION</div></div>
  <div class="agenda-item" style="top:217px"><div class="num"><span>2</span></div><div class="agenda-label">TABLE OF CONTENTS</div></div>
  <div class="agenda-item" style="top:290px"><div class="num"><span>3</span></div><div class="agenda-label">WHO WE ARE</div></div>
  <div class="agenda-item" style="top:363px"><div class="num"><span>4</span></div><div class="agenda-label">WHAT WE DO</div></div>
  <div class="agenda-item" style="top:436px"><div class="num"><span>5</span></div><div class="agenda-label">GRAPH</div></div>
  <div class="agenda-item" style="top:509px"><div class="num"><span>6</span></div><div class="agenda-label">THANK YOU</div></div>
  <div class="page-no">PAGE &nbsp;|&nbsp; 02</div>
  <div class="footer-bar"></div>
</section>

<!-- Slide 3: About us -->
<section class="slide" style="top:1402px">
  <svg class="bg" width="1048" height="590">
    <polygon points="4,0 870,0 959,100 100,100" fill="var(--navy)"/>
    <polygon points="870,0 1048,0 1048,200" fill="var(--tan)"/>
  </svg>
  <div class="header-title">ABOUT US</div>
  <div class="brand header-brand"><span class="mark"></span>RIDGEWARD</div>
  <div class="photo" role="img" aria-label="Two soldiers in helmets and goggles aiming rifles from behind a tree on a forest slope" style="left:60px;top:162px;width:436px;height:361px;background:linear-gradient(135deg,#bdb7aa 0%,#8a7a66 40%,#5a4738 75%,#3c2f26 100%)"></div>
  <div class="abs body-copy" style="left:546px;top:175px;width:442px">
    <p>Lorem ipsum dolor sit amet, consectetur adipiscing elit, sed do eiusmod tempor incididunt ut labore et dolore magna aliqua. Ut enim ad minim veniam, quis nostrud exercitation ullamco laboris nisi ut aliquip ex ea commodo consequat duis aute irure dolor in reprehenderit in voluptate velit esse cillum dolore eu fugiat nulla pariatur.</p>
    <p>Lorem ipsum dolor sit amet, consectetur adipiscing elit, sed do eiusmod tempor incididunt ut labore et dolore magna aliqua. Ut enim ad minim veniam, quis nostrudea.</p>
    <ul class="bullets">
      <li>Lorem ipsum dolor sit amet, consectetur adipiscing elit, sed do eiusmod tempor incididunt ut labore et dolore magna aliqua. Ut enim ad minim veniam, quisea.</li>
      <li>Lorem ipsum dolor sit amet, consectetur adipiscing elit, sed do eiusmod tempor incididunt ut labore et dolore magna aliqua. Ut enim ad minim veniam, quis nostrudea.</li>
    </ul>
  </div>
  <div class="page-no">PAGE &nbsp;|&nbsp; 03</div>
  <div class="footer-bar"></div>
</section>

<!-- Slide 4: What we do -->
<section class="slide" style="top:2059px">
  <svg class="bg" width="1048" height="590">
    <polygon points="4,0 870,0 959,100 100,100" fill="var(--navy)"/>
    <polygon points="870,0 1048,0 1048,200" fill="var(--tan)"/>
    <g fill="none" stroke="var(--tan)" stroke-width="1.5">
      <path d="M521,269 V314"/>
      <path d="M397,321 H425 L463,371"/>
      <path d="M644,321 H617 L579,371"/>
      <path d="M397,497 H425 L463,487"/>
      <path d="M644,497 H617 L579,487"/>
      <polygon points="521,314 636,429 521,544 406,429" fill="var(--light)"/>
    </g>
    <polygon points="521,337 613,429 521,521 429,429" fill="var(--navy)"/>
    <g fill="var(--light)" stroke="var(--tan)" stroke-width="1.5">
      <circle cx="521" cy="314" r="4"/><circle cx="463" cy="371" r="4"/><circle cx="579" cy="371" r="4"/>
      <circle cx="463" cy="487" r="4"/><circle cx="579" cy="487" r="4"/>
      <polygon points="521,193 559,231 521,269 483,231"/>
      <polygon points="359,283 397,321 359,359 321,321"/>
      <polygon points="682,283 720,321 682,359 644,321"/>
      <polygon points="359,459 397,497 359,535 321,497"/>
      <polygon points="682,459 720,497 682,535 644,497"/>
    </g>
    <g fill="none" stroke="var(--ink)" stroke-width="1.3">
      <circle cx="521" cy="227" r="8"/><path d="M509,240 q6,6 12,2 q6,4 12,-4"/>
      <path d="M347,330 L359,310 L371,330 Z M354,322 L359,318 L364,322"/>
      <circle cx="682" cy="321" r="10"/><circle cx="682" cy="321" r="4"/>
      <rect x="351" y="489" width="16" height="16" rx="2"/><path d="M355,497 H363 M359,493 V501"/>
      <path d="M674,508 L682,486 L690,508 M677,500 H687"/>
    </g>
  </svg>
  <div class="header-title">WHAT WE DO</div>
  <div class="brand header-brand"><span class="mark"></span>RIDGEWARD</div>
  <div class="brand abs" style="left:465px;top:417px;font-size:18px;letter-spacing:2px"><span class="mark"></span>RIDGEWARD</div>
  <div class="feature-label" style="left:371px;top:147px;width:300px;text-align:center">LOREM IPSUM DOLOR SIT AMET<br>CONSECTETUR ADIPIEA</div>
  <div class="feature-label" style="left:3px;top:301px;width:300px;text-align:right">LOREM IPSUM DOLOR SIT AMET<br>CONSECTETUR ADIPIEA</div>
  <div class="feature-label" style="left:3px;top:477px;width:300px;text-align:right">LOREM IPSUM DOLOR SIT AMET<br>CONSECTETUR ADIPIEA</div>
  <div class="feature-label" style="left:744px;top:303px;width:300px">LOREM IPSUM DOLOR SIT AMET<br>CONSECTETUR ADIPIEA</div>
  <div class="feature-label" style="left:744px;top:477px;width:300px">LOREM IPSUM DOLOR SIT AMET<br>CONSECTETUR ADIPIEA</div>
  <div class="page-no">PAGE &nbsp;|&nbsp; 04</div>
  <div class="footer-bar"></div>
</section>

<!-- Slide 5: Graph -->
<section class="slide" style="top:2716px">
  <svg class="bg" width="1048" height="590" font-family="Roboto, Arial, sans-serif">
    <polygon points="4,0 870,0 959,100 100,100" fill="var(--navy)"/>
    <polygon points="870,0 1048,0 1048,200" fill="var(--tan)"/>
    <g stroke="#cfc8b3" stroke-width="1">
      <rect x="104" y="177" width="532" height="329" fill="none"/>
      <path d="M180,177V506 M256,177V506 M332,177V506 M408,177V506 M484,177V506 M560,177V506"/>
    </g>
    <g font-size="10" fill="var(--ink)" text-anchor="end">
      <text x="94" y="180">120</text><text x="94" y="235">100</text><text x="94" y="290">80</text>
      <text x="94" y="345">60</text><text x="94" y="399">40</text><text x="94" y="454">20</text><text x="94" y="509">0</text>
    </g>
    <g fill="var(--navy)">
      <rect x="121" y="232" width="14" height="274"/><rect x="197" y="259" width="14" height="247"/>
      <rect x="273" y="369" width="14" height="137"/><rect x="349" y="232" width="14" height="274"/>
      <rect x="425" y="232" width="14" height="274"/><rect x="501" y="341" width="14" height="165"/>
      <rect x="577" y="369" width="14" height="137"/>
    </g>
    <g fill="var(--tan)">
      <rect x="145" y="259" width="14" height="247"/><rect x="221" y="287" width="14" height="219"/>
      <rect x="297" y="232" width="14" height="274"/><rect x="373" y="341" width="14" height="165"/>
      <rect x="449" y="259" width="14" height="247"/><rect x="525" y="300" width="14" height="206"/>
      <rect x="601" y="232" width="14" height="274"/>
    </g>
    <g font-size="10" font-weight="500" fill="var(--ink)" text-anchor="middle">
      <text x="128" y="225">100</text><text x="152" y="252">90</text>
      <text x="204" y="252">90</text><text x="228" y="280">80</text>
      <text x="280" y="362">50</text><text x="304" y="225">100</text>
      <text x="356" y="225">100</text><text x="380" y="334">60</text>
      <text x="432" y="225">100</text><text x="456" y="252">90</text>
      <text x="508" y="334">60</text><text x="532" y="293">75</text>
      <text x="584" y="362">50</text><text x="608" y="225">100</text>
    </g>
    <g font-size="11" font-weight="700" fill="var(--ink)" text-anchor="middle">
      <text x="142" y="524">Sun</text><text x="218" y="524">Mon</text><text x="294" y="524">Tue</text>
      <text x="370" y="524">Wed</text><text x="446" y="524">Thu</text><text x="522" y="524">Fri</text><text x="598" y="524">Sat</text>
    </g>
  </svg>
  <div class="header-title">GRAPH</div>
  <div class="brand header-brand"><span class="mark"></span>RIDGEWARD</div>
  <ul class="bullets abs" style="left:680px;top:185px;width:318px">
    <li>Lorem ipsum dolor sit amet, consectetur adipiscing elit, sed do eiusmod tempor incididunt ut labore et dolore magna aliqua ut enim ad minim veniam.</li>
    <li>Lorem ipsum dolor sit amet, consectetur adipiscing elit, sed do eiusmod tempor incididunt ut labore et dolorea.</li>
    <li>Lorem ipsum dolor sit amet, consectetur adipiscing elit, sed do eiusmod tempor incididunt ut labore et dolore magna aliqua ut enim ad minim veniam.</li>
    <li>Lorem ipsum dolor sit amet, consectetur adipiscing elit, sed do eiusmod tempor incididunt ut labore et dolorea.</li>
  </ul>
  <div class="page-no">PAGE &nbsp;|&nbsp; 05</div>
  <div class="footer-bar"></div>
</section>

<!-- Slide 6: Thank you -->
<section class="slide" style="top:3373px">
  <div class="photo" role="img" aria-label="Soldier crouching in a misty sunlit forest firing a rifle" style="inset:0;background:linear-gradient(160deg,#9fae8a 0%,#5e6f4c 35%,#34402c 70%,#1f2618 100%)"></div>
  <svg class="bg" width="1048" height="590">
    <line x1="714" y1="0" x2="322" y2="590" stroke="var(--cream)" stroke-width="8"/>
    <polygon points="719,0 1048,0 1048,590 327,590" fill="var(--navy)"/>
    <polygon points="521,307 684,590 312,590" fill="var(--tan)"/>
  </svg>
  <div class="abs brand" style="right:58px;top:62px;font-size:24px"><span class="mark"></span>RIDGEWARD</div>
  <div class="abs kicker" style="right:58px;top:188px">RIDGEWARD</div>
  <div class="abs display" style="right:50px;top:210px;font-size:56px">THANK YOU</div>
  <div class="contact" style="top:338px">218, Granite Pass Road, United States<div class="ico"><svg width="14" height="16" viewBox="0 0 14 16"><path d="M7,1 a5,5 0 0 1 5,5 c0,4 -5,9 -5,9 s-5,-5 -5,-9 a5,5 0 0 1 5,-5z" fill="var(--light)"/><circle cx="7" cy="6" r="2" fill="var(--tan)"/></svg></div></div>
  <div class="contact" style="top:398px">+1 (555) 014 2277<div class="ico"><svg width="14" height="14" viewBox="0 0 14 14"><path d="M3,1 l2.5,3 -1.5,1.5 c1,2 2.5,3.5 4.5,4.5 l1.5,-1.5 3,2.5 -1.5,2 c-5,0 -10,-5 -10,-10z" fill="var(--light)"/></svg></div></div>
  <div class="contact" style="top:458px">https://ridgeward.example/<div class="ico"><svg width="16" height="12" viewBox="0 0 16 12"><rect x="1" y="1" width="14" height="10" fill="var(--light)"/><path d="M1,1 L8,7 15,1" fill="none" stroke="var(--tan)" stroke-width="1.3"/></svg></div></div>
  <div class="abs socials" style="left:789px;top:532px">
    <div class="social"></div><div class="social"></div><div class="social"></div><div class="social"></div>
  </div>
</section>

</body>
</html>
```